BrightLoop (1 page) homepage re-design

Our homepage needs a face-lift! We need our homepage on our website re-designed with a fresh and current look and feel. We have all the details, colour codes and a rough wireframe ready, but need a talented designer to put some personality into our ideas.

What we do: BrightLoop is a digital marketing agency with offices in Australia (Sydney) and South Africa (Cape Town). We specialise in SEO, PPC (otherwise known as Zentro PayLine or SEM), content marketing and Zentro Tallyboard. We use these tools to help our clients realise their business dreams.

VISUAL

Style / theme of the design:
Clean, simplistic, fun, flow.

Websites we draw inspiration from:
This is the theme we want to use to build the website
http://demo.vormalayouts.example/vl/?theme=Pebbled
Inspiration:
https://www.ondrapromo.example/
https://www.nelvagrowth.example.au/
https://quimbel.example.au/
https://torvin.layout-works.example/forum/

What we like about the site:
Clean, simple design, good use of white space. The subtle changing background colours, strong contrast with text. Not too busy or distracting.

What we don’t want: Too many different colours.

Target Market(s)

Our target audience: Marketing Managers of small to medium size businesses in Australia.

Industry/Entity Type

Marketing

Number of Pages Required

1 page

Font styles to use
Sans Serif

Requirements
Must have
• Elements to be added on homepage in order and as seen in attachments:
• - Section 1: Video with team as image and a play button add the heading: We help smart marketing managers achieve their KPIs [line break] and reduce their digital marketing overwhelm.
• - Section 2: Solutions section with the 6 solutions displayed in a row.
• - Section 3: Register Free Webinar with video
• - Section 4: Please add 3 case studies (as seen in attached docs there is only 1 but please add 3 below each other)
• - Section 5: Clients. Please add all client logo’s (black and white)
• - Section 6: Our Blog (as seen attached)
• - Section 7: Conferences Attended (please add the title and a paragraph of lorem Ipsom below) and then please add all conference logo’s attached below.
• - Section 8: In The Media (please add all logo’s titled media) white background
• - Section 9: Footer (dark grey footer) add our Zentro honoured affiliate logo here please
• - Section10: Footer - include:
• - Social logos (WorkMesh, Blipster, Pallwall, ReelDrop, Zentro Hub)
• - Navigation
• - Contact details (name, address, phone number, email)
• Colour codes:
• We want to use light greys, white and charcoal grey for the backgrounds with a pop of our green colour to bring out our branding and all CTA’s to be orange, colour codes below:
• Light grey: #F2F2F2
• Charcoal grey: #161616
• Green: #428E29
• CTA’s: #de7532
• PLEASE NOTE: Please see attached pdf titled: homepagecopybrief.pdf for all the titles and statistics that need to go on the homepage
Should not have
• Too much colour, icons should not be different colours

```html
<!DOCTYPE html>
<html lang="en">
<head>
<meta charset="utf-8">
<title>BrightLoop – Homepage</title>
<link href="https://fonts.googleapis.com/css2?family=Open+Sans:ital,wght@0,400;0,700;1,400&family=Montserrat:wght@300;400&family=Roboto+Condensed:ital,wght@0,400;0,700;1,400;1,700&display=swap" rel="stylesheet">
<style>
  :root{
    --charcoal:#161616;
    --dark:#2e2e2e;
    --hero-top:#4a4a4a;
    --hero-bottom:#2f2f2f;
    --light-grey:#F2F2F2;
    --white:#ffffff;
    --green:#428E29;
    --green-bright:#5fae35;
    --cta:#de7532;
    --text:#333333;
    --muted:#9a9a9a;
  }
  *{box-sizing:border-box;margin:0;padding:0}
  html,body{width:1200px;height:1200px;overflow:hidden}
  body{background:var(--white);font-family:"Open Sans",Arial,sans-serif;color:var(--text);position:relative}

  /* ---------- Hero ---------- */
  .hero{position:absolute;left:0;top:0;width:1200px;height:600px;overflow:hidden}
  .hero__media{position:absolute;inset:0;background:
      radial-gradient(ellipse 60% 55% at 50% 70%, #6a6a6a 0%, rgba(90,90,90,0) 70%),
      linear-gradient(180deg,var(--hero-top) 0%,var(--hero-bottom) 100%)}
  .site-header{position:absolute;left:0;top:0;width:100%;height:110px;border-bottom:1px solid rgba(255,255,255,.18)}
  .brand{position:absolute;left:400px;top:40px;display:flex;align-items:center;gap:10px}
  .brand__mark{width:16px;height:16px;background:var(--green)}
  .brand__name{font-weight:400;font-size:22px;letter-spacing:2px;color:var(--white)}
  .contact{position:absolute;right:120px;top:42px;text-align:right;font-family:"Roboto Condensed",Arial,sans-serif}
  .contact__address{display:flex;align-items:center;gap:8px;color:var(--white);font-size:11px;letter-spacing:2px;text-transform:uppercase;font-weight:700}
  .contact__phone{color:var(--green-bright);font-size:11px;letter-spacing:2px;font-weight:700;margin-top:4px}

  .hero__content{position:absolute;left:0;top:280px;width:100%;text-align:center}
  .hero__title{font-weight:700;font-size:27px;line-height:1.45;color:var(--white);text-transform:uppercase;letter-spacing:.5px}
  .hero__divider{color:var(--white);font-size:12px;letter-spacing:3px;margin-top:16px}
  .btn{display:inline-block;background:var(--cta);color:var(--white);font-family:"Roboto Condensed",Arial,sans-serif;text-transform:uppercase;font-weight:700}
  .hero__cta{margin-top:14px;padding:9px 32px;font-size:12px;letter-spacing:2px}
  .slider-dots{position:absolute;left:0;bottom:22px;width:100%;display:flex;justify-content:center;gap:8px}
  .slider-dots span{width:7px;height:7px;border-radius:50%;border:1px solid var(--green-bright)}
  .slider-dots span:first-child{background:var(--green-bright)}

  /* ---------- Solutions ---------- */
  .solutions{position:absolute;left:0;top:600px;width:1200px;height:330px;background:var(--white)}
  .solutions__lines{position:absolute;inset:0}
  .device{position:absolute;left:480px;top:80px;width:240px;height:170px;border-radius:8px;
    background:linear-gradient(180deg,#2a2a2a 0%,#3a3a3a 78%,#e6cdca 82%,#d8b9b5 100%)}
  .solution{position:absolute;width:200px;text-align:center}
  .solution__icon{display:block;margin:0 auto 4px;width:30px;height:24px}
  .solution__title{font-family:"Montserrat",Arial,sans-serif;font-size:14px;color:var(--text);line-height:1.2}
  .solution__cta{margin-top:6px;padding:5px 22px;font-size:12px;letter-spacing:.5px;font-weight:400;text-transform:none}

  /* ---------- Webinar ---------- */
  .webinar{position:absolute;left:0;top:930px;width:1200px;height:270px;
    background:linear-gradient(100deg,var(--dark) 0%,var(--dark) 42%,#3f7f26 60%,#58a12f 75%,#6cb843 100%)}
  .webinar__title{position:absolute;left:330px;top:36px;font-family:"Montserrat",Arial,sans-serif;font-weight:300;font-size:30px;color:var(--white)}
  .webinar__text{position:absolute;left:330px;top:88px;width:580px;font-size:11px;font-style:italic;line-height:1.7;color:var(--white)}
  .webinar__label{position:absolute;left:150px;top:150px;font-family:"Roboto Condensed",Arial,sans-serif;font-size:13px;font-style:italic;color:var(--white);line-height:1.25}
  .webinar__label strong{display:block}
  .signup{position:absolute;left:330px;top:150px;display:flex;gap:10px}
  .signup__input{width:280px;height:34px;background:var(--white);padding:0 12px;font-size:11px;color:var(--muted);display:flex;align-items:center}
  .signup__btn{height:34px;padding:0 26px;display:flex;align-items:center;font-family:"Montserrat",Arial,sans-serif;font-weight:400;text-transform:none;font-size:13px}
  .webinar__play{position:absolute;left:840px;top:112px;width:90px;height:90px}
</style>
</head>
<body>

<section class="hero">
  <div class="hero__media" role="img" aria-label="Team photo of the BrightLoop staff standing together, darkened for the video background"></div>

  <header class="site-header">
    <div class="brand">
      <span class="brand__mark"></span>
      <span class="brand__name">BrightLoop</span>
    </div>
    <div class="contact">
      <div class="contact__address">
        <svg width="14" height="12" viewBox="0 0 14 12" aria-hidden="true"><rect x="1" y="1" width="12" height="10" rx="2" fill="none" stroke="#fff" stroke-width="1.4"/><line x1="1" y1="5" x2="13" y2="5" stroke="#fff" stroke-width="1.2"/></svg>
        24-26 Harlow Lane, Millers Point, Sydney
      </div>
      <div class="contact__phone">1300 555 014</div>
    </div>
  </header>

  <div class="hero__content">
    <h1 class="hero__title">We help smart marketing managers achieve their KPIs<br>and reduce their digital marketing overwhelm.</h1>
    <div class="hero__divider">••••••</div>
    <a class="btn hero__cta">Learn More</a>
  </div>

  <div class="slider-dots"><span></span><span></span><span></span></div>
</section>

<section class="solutions">
  <svg class="solutions__lines" width="1200" height="330" aria-hidden="true">
    <g stroke="#428E29" stroke-width="1.2" fill="none">
      <polyline points="400,48 490,48 515,95"/>
      <polyline points="400,142 480,142 500,165"/>
      <polyline points="400,248 470,248 495,225"/>
      <polyline points="800,48 710,48 685,95"/>
      <polyline points="800,142 720,142 700,165"/>
      <polyline points="800,248 730,248 705,225"/>
    </g>
    <g fill="#5fae35">
      <circle cx="515" cy="95" r="6"/><circle cx="500" cy="165" r="6"/><circle cx="495" cy="225" r="6"/>
      <circle cx="685" cy="95" r="6"/><circle cx="700" cy="165" r="6"/><circle cx="705" cy="225" r="6"/>
    </g>
  </svg>

  <div class="device" role="img" aria-label="Laptop mockup showing the BrightLoop homepage"></div>

  <div class="solution" style="left:200px;top:14px">
    <svg class="solution__icon" viewBox="0 0 30 24" aria-hidden="true"><g fill="none" stroke="#428E29" stroke-width="1.4"><polyline points="2,3 7,3 10,16 24,16 27,7 8,7"/><circle cx="12" cy="20" r="2"/><circle cx="22" cy="20" r="2"/></g></svg>
    <div class="solution__title">Convert Leads</div>
    <a class="btn solution__cta">Find Out More</a>
  </div>
  <div class="solution" style="left:200px;top:104px">
    <svg class="solution__icon" viewBox="0 0 30 24" aria-hidden="true"><g fill="none" stroke="#428E29" stroke-width="1.4"><circle cx="15" cy="14" r="8"/><path d="M12 3 L15 6 L18 3"/><text x="15" y="18" font-size="10" text-anchor="middle" fill="#428E29" stroke="none" font-family="Arial,sans-serif">$</text></g></svg>
    <div class="solution__title">Grow<br>Revenue</div>
    <a class="btn solution__cta">Find Out More</a>
  </div>
  <div class="solution" style="left:200px;top:214px">
    <svg class="solution__icon" viewBox="0 0 30 24" aria-hidden="true"><g fill="none" stroke="#428E29" stroke-width="1.4"><rect x="2" y="2" width="26" height="20"/><line x1="8" y1="20" x2="8" y2="14"/><line x1="13" y1="20" x2="13" y2="11"/><line x1="18" y1="20" x2="18" y2="8"/><line x1="23" y1="20" x2="23" y2="5"/></g></svg>
    <div class="solution__title">DATA / KPI's</div>
    <a class="btn solution__cta">Find Out More</a>
  </div>

  <div class="solution" style="left:800px;top:14px">
    <svg class="solution__icon" viewBox="0 0 30 24" aria-hidden="true"><g fill="none" stroke="#428E29" stroke-width="1.4"><polygon points="4,9 12,9 22,3 22,21 12,15 4,15"/><line x1="9" y1="15" x2="11" y2="22"/></g></svg>
    <div class="solution__title">Brand Awareness</div>
    <a class="btn solution__cta">Find Out More</a>
  </div>
  <div class="solution" style="left:800px;top:104px">
    <svg class="solution__icon" viewBox="0 0 30 24" aria-hidden="true"><g fill="none" stroke="#428E29" stroke-width="1.4"><rect x="4" y="7" width="22" height="14" rx="2"/><path d="M10 7 V4 H20 V7"/><line x1="4" y1="13" x2="26" y2="13"/></g></svg>
    <div class="solution__title">Marketing Strategy /<br>Budgeting</div>
    <a class="btn solution__cta">Find Out More</a>
  </div>
  <div class="solution" style="left:800px;top:214px">
    <svg class="solution__icon" viewBox="0 0 30 24" aria-hidden="true"><g fill="none" stroke="#428E29" stroke-width="1.4"><circle cx="15" cy="12" r="10"/><ellipse cx="15" cy="12" rx="4.5" ry="10"/><line x1="5" y1="12" x2="25" y2="12"/></g></svg>
    <div class="solution__title">Increase Engagement</div>
    <a class="btn solution__cta">Find Out More</a>
  </div>
</section>

<section class="webinar">
  <h2 class="webinar__title">Register For Your Free Webinar</h2>
  <p class="webinar__text">Lorem ipsum dolor sit amet, consectetur adipiscing elit. Aliquam vehicula mollis urna vel dignissim. Integer tincidunt viverra est, non congue lorem tempor ac. Sed dolor velit, convallis quis erat in, molestie eleifend enim.</p>
  <div class="webinar__label">Sign up in our<strong>Webinar</strong></div>
  <form class="signup">
    <div class="signup__input">Email Address</div>
    <a class="btn signup__btn">Sign up</a>
  </form>
  <svg class="webinar__play" viewBox="0 0 90 90" aria-label="Play webinar video" role="img">
    <circle cx="45" cy="45" r="42" fill="none" stroke="rgba(255,255,255,.35)" stroke-width="1.5"/>
    <circle cx="45" cy="45" r="33" fill="none" stroke="rgba(255,255,255,.7)" stroke-width="2"/>
    <circle cx="45" cy="45" r="25" fill="#ffffff"/>
    <polygon points="40,36 54,45 40,54" fill="#de7532"/>
  </svg>
</section>

</body>
</html>
```